THE AMBER HEARTH SESSIONS - CD COVER DESIGN

I am a professional female vocalist based in Devon, UK. I require a CD COVER for a CHRISTMAS album of mixed genre tracks - jazz/big-band/country/gospel/acoustic songs, all with a traditional 'Festive/Christmas' theme.

Cover to fit STANDARD CD JEWEL CASE comprising: FRONT COVER INLAY / INSIDE FRONT / REAR INLAY and SPINE. Plus CD FACE.

The design needs to incorporate the 2 publicity photographs attached. CD1 (wearing WHITE FUR JACKET) is the main picture and preferred choice for front cover pic. CD2 (wearing RED DRESS) can be used anywhere in the design.

CD WORDING: Please see attached info. The track listing is also provided on a separate sheet.
Updates

Sick

Target Market(s)

Festive music market!

Industry/Entity Type

It Professional

Font styles to use
Serif
Sans Serif
Decorative
Script

Colors
ec1f27

Requirements
Must have
• CHRISTMAS / FESTIVE THEME!
• Must incorporate the 2 publicity photographs attached.
• TRACK LISTING to feature on CD FACE and REAR INLAY.
• CD WORDING attached.
Should not have
• Not keen on 'cartoon type' images - prefer more traditional.

```html
<!DOCTYPE html>
<html lang="en">
<head>
<meta charset="utf-8">
<title>The Amber Hearth Sessions – CD Artwork</title>
<link href="https://fonts.googleapis.com/css2?family=Great+Vibes&family=Lato:wght@700;900&family=Bebas+Neue&family=Arimo:wght@400;700&display=swap" rel="stylesheet">
<style>
  :root {
    --page: #ffffff;
    --wine: #5a0b14;
    --wine-deep: #3a0509;
    --festive-red: #ec1f27;
    --satin-red: #c4121d;
    --crimson: #a3101c;
    --cream: #efe6d8;
    --fur: #e8dcc6;
    --hair: #f1e7cf;
    --skin: #e2bfa6;
    --white: #ffffff;
    --silver: #ececec;
    --track-num: #c9e04c;
  }
  html, body { margin: 0; padding: 0; overflow: hidden; background: var(--page); }
  .canvas { position: relative; width: 1200px; height: 1200px; overflow: hidden; background: var(--page); }

  .panel { position: absolute; overflow: hidden; }
  .fill { position: absolute; }
  .script-title {
    margin: 0; font-weight: 400;
    font-family: "Great Vibes", cursive;
    color: var(--silver);
    line-height: 0.78;
    text-shadow: 0 2px 3px rgba(0,0,0,0.45);
    white-space: nowrap;
  }
  .script-title span { display: block; }
  .track-text { font-family: "Bebas Neue", sans-serif; text-transform: uppercase; color: var(--white); }
  .track-text b { color: var(--track-num); font-weight: 400; font-size: 0.72em; }

  /* Front cover */
  .front { left: 41px; top: 49px; width: 528px; height: 527px;
    background: linear-gradient(100deg, #2a1410 0%, #5c1018 40%, #8a111c 70%, #6a0a14 100%); }
  .front-tree { left: 0; top: 0; width: 150px; height: 300px;
    background: radial-gradient(ellipse at 40% 50%, #4a1a12 0%, #2a120e 60%, rgba(42,18,14,0) 100%); }
  .front-portrait { left: 0; top: 20px; width: 400px; height: 507px;
    border-radius: 48% 52% 0 0 / 38% 40% 0 0;
    background:
      radial-gradient(ellipse 30% 26% at 50% 40%, var(--skin) 0%, var(--skin) 55%, rgba(226,191,166,0) 100%),
      radial-gradient(ellipse 48% 42% at 50% 36%, var(--hair) 0%, var(--hair) 60%, rgba(241,231,207,0) 100%),
      linear-gradient(180deg, rgba(232,220,198,0) 45%, var(--fur) 70%, #d9cbb0 100%); }
  .front-bow { left: 270px; top: 300px; width: 290px; height: 250px;
    border-radius: 50% 45% 40% 50%;
    background: radial-gradient(ellipse at 45% 45%, var(--festive-red) 0%, var(--satin-red) 45%, #7c0a12 85%, rgba(124,10,18,0) 100%); }
  .front-artist {
    position: absolute; right: 26px; top: 20px; margin: 0;
    font-family: "Lato", sans-serif; font-weight: 900; font-size: 26px;
    color: var(--white); letter-spacing: 0.2px;
  }
  .front .script-title { position: absolute; right: 20px; top: 350px; text-align: right; }
  .front .t-lead { font-size: 44px; padding-right: 60px; }
  .front .t-main { font-size: 82px; }
  .front .t-tail { font-size: 52px; }

  /* Inside front */
  .inside { left: 646px; top: 50px; width: 526px; height: 526px;
    background: linear-gradient(135deg, #a0101b 0%, #7a0b15 55%, #4a0710 100%); }
  .inside-pattern { left: 0; top: 0; width: 526px; height: 526px;
    background:
      radial-gradient(circle at 8% 15%, rgba(236,31,39,0.35) 0%, rgba(236,31,39,0) 18%),
      radial-gradient(circle at 92% 85%, rgba(236,31,39,0.35) 0%, rgba(236,31,39,0) 22%),
      radial-gradient(circle at 12% 70%, rgba(255,255,255,0.08) 0%, rgba(255,255,255,0) 16%); }
  .inside-portrait { left: 0; top: 20px; width: 370px; height: 506px;
    border-radius: 46% 54% 0 0 / 30% 34% 0 0;
    background:
      radial-gradient(ellipse 20% 17% at 55% 50%, var(--skin) 0%, var(--skin) 60%, rgba(226,191,166,0) 100%),
      radial-gradient(ellipse 34% 29% at 50% 37%, var(--hair) 0%, var(--hair) 62%, rgba(241,231,207,0) 100%),
      linear-gradient(180deg, rgba(179,18,29,0) 52%, #b3121d 70%, #9a0e19 100%); }
  .tracklist {
    position: absolute; right: 20px; top: 24px; width: 210px;
    font-size: 19px; line-height: 16.4px; text-align: right;
  }

  /* Rear inlay */
  .rear {
    left: 26px; top: 624px; width: 592px; height: 518px;
    background: radial-gradient(ellipse 80% 70% at 55% 40%, #8e1421 0%, #5e0b15 60%, var(--wine-deep) 100%);
  }
  .rear-pattern { left: 440px; top: 140px; width: 160px; height: 330px;
    border-radius: 40%;
    background: radial-gradient(ellipse at 60% 50%, rgba(255,255,255,0.1) 0%, rgba(255,255,255,0) 70%); }
  .spine {
    position: absolute; left: 0; top: 0; width: 40px; height: 100%;
    border-right: 1px solid rgba(255,255,255,0.1);
  }
  .spine-text {
    position: absolute; left: 20px; bottom: 20px;
    transform-origin: left bottom; transform: rotate(-90deg) translateY(50%);
    white-space: nowrap; display: flex; align-items: center; gap: 30px;
  }
  .spine-title { font-family: "Great Vibes", cursive; font-size: 30px; color: var(--silver); }
  .spine-artist { font-family: "Lato", sans-serif; font-weight: 900; font-size: 27px; color: var(--white); }
  .rear-info {
    position: absolute; left: 40px; right: 0; top: 50px;
    font-family: "Arimo", sans-serif; font-size: 13.6px; line-height: 16.8px;
    color: var(--white); text-align: center;
  }
  .rear-info p { margin: 0; }
  .guild { font-weight: 700; margin: 4px 0 6px !important; }
  .social { display: flex; justify-content: center; gap: 2px; margin-top: 7px; }
  .social span { width: 16px; height: 16px; border-radius: 50%; background: var(--white); }
  .rear .script-title { position: absolute; left: 150px; top: 332px; text-align: right; }
  .rear .t-lead { font-size: 46px; padding-right: 120px; }
  .rear .t-main { font-size: 86px; }
  .rear .t-tail { font-size: 54px; }

  /* Disc */
  .disc { left: 646px; top: 624px; width: 528px; height: 528px; border-radius: 50%; }
  .disc-face {
    position: absolute; inset: 0; border-radius: 50%;
    background:
      radial-gradient(circle at 18% 65%, #d0222b 0%, rgba(208,34,43,0) 35%),
      radial-gradient(circle at 50% 50%, #9b1420 0%, #6a0d16 70%, #4a0810 100%);
  }
  .disc-pattern { inset: 0; border-radius: 50%;
    background:
      radial-gradient(circle at 25% 18%, rgba(255,255,255,0.08) 0%, rgba(255,255,255,0) 20%),
      radial-gradient(circle at 92% 72%, rgba(236,31,39,0.45) 0%, rgba(236,31,39,0) 18%),
      radial-gradient(circle at 40% 92%, rgba(236,31,39,0.35) 0%, rgba(236,31,39,0) 20%); }
  .disc .script-title { position: absolute; left: 0; right: 0; top: 30px; text-align: center; }
  .disc .t-lead { font-size: 40px; padding-right: 90px; }
  .disc .t-main { font-size: 76px; }
  .disc .t-tail { font-size: 48px; padding-left: 110px; }
  .disc-hole {
    position: absolute; left: 230px; top: 230px; width: 68px; height: 68px;
    border-radius: 50%; background: var(--page);
  }
  .disc-tracks {
    position: absolute; left: 110px; width: 308px; top: 368px;
    font-size: 12.2px; line-height: 11.5px; text-align: center;
  }
</style>
</head>
<body>
<div class="canvas">

  <section class="panel front">
    <div class="fill front-tree" role="img" aria-label="Dark Christmas tree with red baubles behind the singer"></div>
    <div class="fill front-portrait" role="img" aria-label="Publicity photo of the singer with platinum curls, white fur jacket and white lace gloves"></div>
    <div class="fill front-bow" role="img" aria-label="Large red satin bow"></div>
    <h2 class="front-artist">HOLLY VANCE</h2>
    <h1 class="script-title"><span class="t-lead">The Amber</span><span class="t-main">Hearth</span><span class="t-tail">Sessions</span></h1>
  </section>

  <section class="panel inside">
    <div class="fill inside-pattern" role="img" aria-label="Faint red poinsettia pattern"></div>
    <div class="fill inside-portrait" role="img" aria-label="Publicity photo of the singer in a red off-shoulder dress with a white flower in her hair"></div>
    <div class="tracklist track-text">
      <b>1.</b> Jingle Bells <b>2.</b> Hark The Herald Angels Sing <b>3.</b> Do You Hear What I Hear <b>4.</b> Winter Wonderland <b>5.</b> I've Got My Love To Keep Me A Warm <b>6.</b> The First Noel <b>7.</b> Little Drummer Boy <b>8.</b> Baby Its Cold Outside <b>9.</b> Tennessee Christmas <b>10.</b> Have A Holly Jolly Christmas <b>11.</b> Santa Baby <b>12.</b> Blue Christmas <b>13.</b> The Christmas Song <b>14.</b> O Come All Ye Faithful <b>15.</b> Have Yourself A Merry Little Christmas <b>16.</b> Let It Snow <b>17.</b> In The Bleak Midwinter <b>18.</b> Mary's Boy Child <b>19.</b> White Christmas <b>20.</b> Santa Claus Is Comin' In A Boogie Woogie Choo-Choo Train
    </div>
  </section>

  <section class="panel rear">
    <div class="fill rear-pattern" role="img" aria-label="Faint snowflake and star pattern"></div>
    <div class="spine">
      <div class="spine-text">
        <span class="spine-title">The Amber Hearth Sessions</span>
        <span class="spine-artist">HOLLY VANCE</span>
      </div>
    </div>
    <div class="rear-info">
      <p>HOLLY VANCE is a British PROFESSIONAL SINGER</p>
      <p>and award winning International MULTI-TRIBUTE ARTISTE.</p>
      <p>Available for bookings in the UK &amp; WORLDWIDE.</p>
      <p>Member of BRITISH STAGEGUILD.</p>
      <p class="guild">Stageguild</p>
      <p>BOOKING ENQUIRIES:</p>
      <p>Telephone: 07000 555 214</p>
      <p>Email: bookings@hollyvance.example</p>
      <div class="social"><span></span><span></span><span></span><span></span><span></span><span></span><span></span></div>
    </div>
    <h2 class="script-title"><span class="t-lead">The Amber</span><span class="t-main">Hearth</span><span class="t-tail">Sessions</span></h2>
  </section>

  <section class="panel disc">
    <div class="disc-face"></div>
    <div class="fill disc-pattern" role="img" aria-label="Faint snowflake pattern across the disc"></div>
    <h2 class="script-title"><span class="t-lead">The Amber</span><span class="t-main">Hearth</span><span class="t-tail">Sessions</span></h2>
    <div class="disc-hole"></div>
    <div class="disc-tracks track-text">
      <b>1.</b> Jingle Bells <b>2.</b> Hark The Herald Angels Sing <b>3.</b> Do You Hear What I Hear <b>4.</b> Winter Wonderland <b>5.</b> I've Got My Love To Keep Me A Warm <b>6.</b> The First Noel <b>7.</b> Little Drummer Boy <b>8.</b> Baby Its Cold Outside <b>9.</b> Tennessee Christmas <b>10.</b> Have A Holly Jolly Christmas <b>11.</b> Santa Baby <b>12.</b> Blue Christmas <b>13.</b> The Christmas Song <b>14.</b> O Come All Ye Faithful <b>15.</b> Have Yourself A Merry Little Christmas <b>16.</b> Let It Snow <b>17.</b> In The Bleak Midwinter <b>18.</b> Mary's Boy Child <b>19.</b> White Christmas <b>20.</b> Santa Claus Is Comin' In A Boogie Woogie Choo-Choo Train
    </div>
  </section>

</div>
</body>
</html>
```